今回はコーポレートサイトのTOPページのデザインをお願いしたく思います。

【素材】
素材に関しては、ロゴや写真等は現在準備中でして、
デザインの際は仮のオブジェクトを入れて対応して頂ければと思います。

【サイト構成】
サイトの構成については、ラフを書きましたので下記URLからダウンロードお願いします。
http://qvn.jp/PbLwoR

※PCを想定したデザインでお願いいたします。

【イメージ】
以下が現在の「アオバエステート株式会社」のコーポレートサイトになります。
http://www.aoba-estate.co.jp/

今回ご提案いただく新しいサイトのデザインは上記のものから一新して

1.スタイリッシュ
2.NY
3.最先端
4.近未来
5.エネルギッシュ
6.エキサイティング
7.自由
8.それでいてシンプル

なイメージ、従来の不動産会社のイメージに囚われないものにしたく思います。

【参考サイト】
https://www.kumonomi.co.jp/

1ページ
グレー系
今回のデザインで採用させて頂いた方には、
コーポレートサイトの「代表メッセージ」「ニュース」「投資実績」の他3ページのデザインやコーディングなど、他のお仕事に関してもご相談させて頂ければと思います。
(もちろん当案件のみご希望の方からも募集しており、採用有無には関係ありません。)

色のコンセプトと対応の早さ、デザインの良さで決定致しました。

皆さま、お忙しい所多くのご提案を頂きまして誠にありがとうございます。
また何かございましたらお願いをさせて頂きますので引き続き宜しくお願い致します。

```html
<!DOCTYPE html>
<html lang="ja">
<head>
<meta charset="utf-8">
<title>アオバエステート</title>
<link rel="stylesheet" href="https://fonts.googleapis.com/css2?family=Cormorant+Garamond:wght@400;500;600&family=Noto+Serif+JP:wght@400;500;600&family=Noto+Sans+JP:wght@400;500&display=swap">
<style>
:root{
  --ink:#22242a;
  --text:#333;
  --muted:#777;
  --line:#cfcfcf;
  --paper:#f6f6f6;
  --white:#fff;
}
*{margin:0;padding:0;box-sizing:border-box}
html,body{width:1200px;height:5004px;overflow:hidden}
body{background:var(--paper);color:var(--text);font-family:"Noto Serif JP",serif;position:relative}
.abs{position:absolute}

/* header */
.hero{left:0;top:0;width:1200px;height:620px;background:linear-gradient(180deg,#5a5f68 0%,#8d939b 35%,#b9bec4 55%,#6d727a 100%)}
.hero-shade{left:0;top:0;width:1200px;height:620px;background:linear-gradient(90deg,rgba(20,22,26,.55),rgba(20,22,26,.1) 50%,rgba(20,22,26,.55))}
.topbar{left:0;top:0;width:1200px;height:44px;background:rgba(28,30,35,.92);display:flex;align-items:center;padding-left:22px}
.brand{color:var(--white);font-family:"Noto Serif JP",serif;font-size:17px;font-weight:500;letter-spacing:.02em;white-space:nowrap}
.nav{right:0;top:0;height:44px;display:flex;align-items:center}
.nav a{color:var(--white);font-size:11px;letter-spacing:.12em;text-decoration:none;padding:0 28px;font-family:"Cormorant Garamond",serif}
.nav a.contact{background:var(--white);color:var(--ink);height:44px;line-height:44px;padding:0 26px;margin-left:10px}
.dropdown{left:892px;top:44px;width:96px;background:rgba(28,30,35,.92);padding:6px 0}
.dropdown span{display:block;color:#ddd;font-size:9px;padding:7px 12px;font-family:"Noto Sans JP",sans-serif}
.hero-logo{left:0;top:166px;width:1200px;text-align:center;color:var(--white);font-family:"Noto Serif JP",serif;font-size:44px;font-weight:500;letter-spacing:.04em}

.philosophy{left:220px;top:620px;width:760px;height:220px;background:var(--ink);color:var(--white);text-align:center;padding-top:44px}
.philosophy .eyebrow{font-family:"Cormorant Garamond",serif;letter-spacing:.3em;font-size:15px}
.philosophy .rule{width:300px;height:1px;background:#666;margin:14px auto 18px}
.philosophy h2{font-weight:500;font-size:22px;letter-spacing:.15em}
.philosophy p{font-size:10px;color:#bbb;margin-top:26px;letter-spacing:.06em}

/* works */
.photo{background:linear-gradient(160deg,#9ea3aa,#d9dcdf 60%,#8b9097)}
.works-hero{left:192px;top:872px;width:336px;height:468px;background:linear-gradient(180deg,#c9ced3,#7d8692 70%,#5c6570)}
.section-title{font-family:"Cormorant Garamond",serif;letter-spacing:.25em;font-size:34px;font-weight:500;color:var(--ink)}
.section-title-rule{height:1px;background:var(--ink)}
.works-lead{left:620px;top:1020px;width:420px;font-size:12px;line-height:1.9;color:#555}
.btn{display:flex;align-items:center;justify-content:center;font-size:11px;letter-spacing:.12em;height:34px;width:156px}
.btn.dark{background:var(--ink);color:var(--white)}
.btn.line{border:1px solid var(--ink);color:var(--ink);background:var(--white)}

.work-photo{height:320px}
.tag{background:var(--ink);color:var(--white);font-size:11px;padding:7px 18px;letter-spacing:.1em}
.bar{height:6px;background:var(--ink)}
.date{font-size:10px;color:var(--muted);font-family:"Cormorant Garamond",serif;letter-spacing:.1em}
.work-title{font-size:18px;font-weight:500;color:var(--ink);padding-bottom:8px;border-bottom:1px solid var(--ink);letter-spacing:.03em;line-height:1.5}
.work-desc{font-size:11px;line-height:1.9;color:#555}
.spec{font-size:11px;color:var(--text);border-collapse:collapse}
.spec td{padding:8px 0;border-bottom:1px solid var(--line)}
.spec td:first-child{width:110px;color:#555}
.more{width:120px;height:32px;background:var(--ink);color:var(--white);font-family:"Cormorant Garamond",serif;font-size:14px;display:flex;align-items:center;padding-left:34px;letter-spacing:.1em}
.more-line{height:1px;background:var(--ink)}

/* profile */
.profile{left:0;top:3040px;width:1200px;height:600px;background:linear-gradient(180deg,#2d3a44 0%,#3e4b55 40%,#262c33 100%)}
.profile-shade{left:0;top:3040px;width:1200px;height:600px;background:rgba(20,22,26,.55)}
.ptable{font-size:11px;color:#e7e7e7;border-collapse:collapse;width:470px}
.ptable td{padding:10px 0;border-bottom:1px solid rgba(255,255,255,.35);vertical-align:top;line-height:1.6}
.ptable td:first-child{width:120px}

/* news */
.news-row{display:flex;font-size:11px;border-bottom:1px solid var(--line);padding:12px 0;width:620px}
.news-row .d{width:110px;font-family:"Cormorant Garamond",serif;color:#555}
.news-row .c{width:70px;color:#555}
.viewall{left:100px;top:3852px;width:136px;height:28px;border:1px solid var(--ink);font-size:11px;display:flex;align-items:center;padding-left:18px;background:var(--white)}

.map{left:140px;top:4080px;width:920px;height:580px;background:linear-gradient(135deg,#8a8a8a,#a4a4a4 40%,#929292 70%,#7e7e7e)}
.pin{left:574px;top:4326px;width:52px;height:52px;transform:rotate(45deg);background:var(--white);border:1px solid var(--ink)}
.pin-label{left:564px;top:4344px;width:72px;text-align:center;font-size:9px;color:var(--ink)}

footer{left:0;top:4720px;width:1200px;height:284px;background:var(--ink);color:var(--white)}
.foot-info{font-size:10px;line-height:1.9;color:#ddd}
.foot-nav{display:flex;align-items:center}
.foot-nav a{color:var(--white);font-family:"Cormorant Garamond",serif;font-size:11px;letter-spacing:.12em;text-decoration:none;padding:0 28px}
.foot-nav a.contact{background:var(--white);color:var(--ink);height:44px;line-height:44px;padding:0 26px}
.copy{font-size:9px;color:#999}
</style>
</head>
<body>

<header>
  <div class="abs hero" role="img" aria-label="見上げた高層ビル群と曇り空の写真"></div>
  <div class="abs hero-shade"></div>
  <div class="abs topbar"><div class="brand">アオバエステート</div></div>
  <nav class="abs nav">
    <a href="#">HOME</a><a href="#">ABOUT ▾</a><a href="#">WORKS</a><a href="#">NEWS</a><a href="#" class="contact">CONTACT</a>
  </nav>
  <div class="abs dropdown"><span>代表挨拶</span><span>会社概要</span></div>
  <div class="abs hero-logo">アオバエステート</div>
</header>

<section class="abs philosophy">
  <div class="eyebrow">PHILOSOPHY</div>
  <div class="rule"></div>
  <h2>不動産の新しい"未来"をつくる</h2>
  <p>アオバエステート株式会社は不動産の新しい未来をつくります。不動産の新しい未来を創造します。</p>
</section>

<!-- works -->
<div class="abs works-hero" role="img" aria-label="川沿いに建つタワーマンションの写真"></div>
<h2 class="abs section-title" style="left:620px;top:930px">WORKS</h2>
<div class="abs section-title-rule" style="left:620px;top:986px;width:440px"></div>
<p class="abs works-lead">アオバエステートは、住宅用地の取得から企画・設計・施工まで一貫して手掛けています。都市に新しい価値を提供し、暮らしの未来をつくります。<br>テキストテキストテキストテキストテキストテキスト<br>テキストテキストテキストテキストテキスト</p>
<div class="abs btn dark" style="left:620px;top:1170px">投資実績</div>
<div class="abs btn line" style="left:858px;top:1170px">物件紹介</div>

<!-- work 1 -->
<div class="abs photo work-photo" style="left:140px;top:1420px;width:440px" role="img" aria-label="モダンな平屋住宅の外観写真"></div>
<div class="abs tag" style="left:140px;top:1420px">エグゼクティブ</div>
<div class="abs bar" style="left:140px;top:1740px;width:30px"></div>
<div class="abs date" style="left:620px;top:1500px">2019.09.20</div>
<h3 class="abs work-title" style="left:620px;top:1518px;width:420px">渋谷区青葉台北地【960坪】</h3>
<p class="abs work-desc" style="left:720px;top:1572px;width:320px">閑静な住宅地に位置する約960坪の土地を取得。ゆとりある敷地を活かした開発を計画しています。</p>
<table class="abs spec" style="left:620px;top:1640px;width:420px">
  <tr><td>所在地</td><td>東京都渋谷区青葉台4-5-6</td></tr>
  <tr><td>種別</td><td>土地</td></tr>
  <tr><td>土地面積</td><td>3174㎡（960坪）</td></tr>
</table>
<div class="abs more" style="left:620px;top:1784px">More</div>
<div class="abs more-line" style="left:740px;top:1800px;width:100px"></div>

<!-- work 2 -->
<div class="abs date" style="left:140px;top:1886px">2019.08.15</div>
<h3 class="abs work-title" style="left:140px;top:1904px;width:440px">若葉台戸建住宅・建築条件付き土地</h3>
<p class="abs work-desc" style="left:240px;top:1958px;width:320px">緑豊かな住環境に、建築条件付きの区画をご用意しました。自由設計で理想の住まいを実現できます。</p>
<table class="abs spec" style="left:140px;top:2040px;width:440px">
  <tr><td>所在地</td><td>東京都目黒区若葉台2-8</td></tr>
  <tr><td>種別</td><td>戸建住宅</td></tr>
  <tr><td>土地面積</td><td>165.2㎡（50坪）</td></tr>
</table>
<div class="abs more" style="left:140px;top:2304px">More</div>
<div class="abs more-line" style="left:260px;top:2320px;width:100px"></div>
<div class="abs photo work-photo" style="left:652px;top:2020px;width:408px" role="img" aria-label="ガレージ付き二階建て住宅の外観写真"></div>
<div class="abs tag" style="left:652px;top:2020px">新築物件</div>
<div class="abs bar" style="left:1030px;top:2340px;width:30px"></div>

<!-- work 3 -->
<div class="abs photo work-photo" style="left:140px;top:2540px;width:440px" role="img" aria-label="ガラス張りのモダン住宅と庭の写真"></div>
<div class="abs tag" style="left:140px;top:2540px">完成物件</div>
<div class="abs bar" style="left:140px;top:2860px;width:30px"></div>
<div class="abs date" style="left:620px;top:2506px">2019.07.01</div>
<h3 class="abs work-title" style="left:620px;top:2524px;width:420px">アオバエステート株式会社新設<br>完全セキュリティ付きマンション竣工</h3>
<p class="abs work-desc" style="left:720px;top:2610px;width:320px">最新のセキュリティ設備を備えた新築マンションが竣工しました。安心と快適を両立した住まいです。</p>
<table class="abs spec" style="left:620px;top:2690px;width:420px">
  <tr><td>所在地</td><td>東京都港区青山1-9</td></tr>
  <tr><td>種別</td><td>マンション</td></tr>
  <tr><td>土地面積</td><td>660㎡（200坪）</td></tr>
</table>
<div class="abs more" style="left:620px;top:2830px">More</div>
<div class="abs more-line" style="left:740px;top:2846px;width:100px"></div>

<!-- profile -->
<div class="abs profile" role="img" aria-label="夜明けの都市の俯瞰写真"></div>
<div class="abs profile-shade"></div>
<h2 class="abs section-title" style="left:0;top:3096px;width:1200px;text-align:center;color:#fff">PLOFILE</h2>
<div class="abs" style="left:500px;top:3150px;width:200px;height:1px;background:rgba(255,255,255,.6)"></div>
<table class="abs ptable" style="left:100px;top:3200px">
  <tr><td>商号</td><td>アオバエステート株式会社</td></tr>
  <tr><td>所在地</td><td>東京都渋谷区青葉台1-2-3 アオバビル5F</td></tr>
  <tr><td>資本金</td><td>1000万円</td></tr>
  <tr><td>代表</td><td>代表取締役　青葉 一郎</td></tr>
  <tr><td>事業</td><td>不動産売買・仲介・管理</td></tr>
  <tr><td>設立</td><td>2010年4月</td></tr>
</table>
<table class="abs ptable" style="left:630px;top:3200px">
  <tr><td>従業員</td><td>15名</td></tr>
  <tr><td>宅地建物取引業免許</td><td>東京都知事（2）第00000号</td></tr>
  <tr><td>加盟団体</td><td>公益社団法人 不動産協会</td></tr>
  <tr><td>取引銀行</td><td>青葉銀行 渋谷支店<br>若葉信用金庫 本店</td></tr>
  <tr><td>事業内容</td><td>土地の仕入れ・企画開発<br>収益不動産の売買・仲介<br>不動産コンサルティング</td></tr>
</table>

<!-- news -->
<h2 class="abs section-title" style="left:100px;top:3760px">NWES</h2>
<div class="abs section-title-rule" style="left:100px;top:3812px;width:240px"></div>
<div class="abs viewall">一覧へ →</div>
<div class="abs" style="left:440px;top:3760px">
  <div class="news-row"><span class="d">2019.09.20</span><span class="c">お知らせ</span><span>新しい物件情報を公開しました。詳細は物件紹介ページをご覧ください。</span></div>
  <div class="news-row"><span class="d">2019.09.01</span><span class="c">お知らせ</span><span>ホームページをリニューアルしました。</span></div>
  <div class="news-row"><span class="d">2019.08.15</span><span class="c">お知らせ</span><span>夏季休業期間のお知らせ</span></div>
</div>

<!-- access -->
<h2 class="abs section-title" style="left:0;top:3990px;width:1200px;text-align:center;font-size:28px">ACCES</h2>
<div class="abs" style="left:540px;top:4038px;width:120px;height:1px;background:var(--ink)"></div>
<div class="abs map" role="img" aria-label="本社周辺の地図"></div>
<div class="abs pin"></div>
<div class="abs pin-label">本社</div>

<!-- footer -->
<footer class="abs">
  <div class="abs brand" style="left:40px;top:42px;font-size:20px">アオバエステート</div>
  <div class="abs foot-info" style="left:40px;top:100px">〒150-0032　TEL:03-1234-5678　FAX:03-1234-5679<br>東京都渋谷区青葉台1-2-3 アオバビル5F</div>
  <nav class="abs foot-nav" style="right:40px;top:78px">
    <a href="#">HOME</a><a href="#">ABOUT</a><a href="#">WORKS</a><a href="#">NEWS</a><a href="#" class="contact">CONTACT</a>
  </nav>
  <div class="abs copy" style="left:40px;top:180px">copyright アオバエステート</div>
</footer>

</body>
</html>
```